SilverLedgerOak - Double Sided Business Card

We are looking for design options or our business cards. We are a Business Solutions and HR solutions Provider - the theme is business, for this card.

Our brand colours are represented within our logo.

Details needed to be put on the front of the business card are:

Employees name: [Sample Name]
Role: [Sample Role]

Address: Suite 4 - Level 3/48 Halloran Avenue Parramatta NSW 2150
M: 0000 000 000
P: 1300 847 213
F: 1300 847 286
E: sample@silverledgeroak.com.au
www.silverledgeroak.com.au
Updates

Reason: Hello, could we please increase our deadline by 5 days. Thanking you, Tess

Target Market(s)

Business Owners, also Candidates looking for Employment

Industry/Entity Type

Business

Contact Information for Business Card

Role: [Sample Role]

M: 0000 000 000
P: 1300 847 213
F: 1300 847 286

Font styles to use
Sans Serif

Colors
3276b5
3176b5
0455a3
85abd2
cfdeed
ffffff
000000
1b1b1b
757575

Requirements
Must have
• Details needed to be put on the front of the business card are:
• Employees name: [Sample Name]
• Role: [Sample Role]
• Address: Suite 4 - Level 3/48 Halloran Avenue Parramatta NSW 2150
• M: 0000 000 000
• P: 1300 847 213
• F: 1300 847 286
• E: sample@silverledgeroak.com.au
• www.silverledgeroak.com.au
Nice to have
• Simplicity, clean and professional.

```html
<!DOCTYPE html>
<html lang="en">
<head>
<meta charset="utf-8">
<title>SilverLedgerOak Business Card</title>
<link href="https://fonts.googleapis.com/css2?family=Montserrat:wght@400;600;700&display=swap" rel="stylesheet">
<style>
  :root {
    --blue-mid: #1b77be;
    --blue-dark: #0455a3;
    --blue-light: #85abd2;
    --white: #ffffff;
    --black: #000000;
    --canvas: #ffffff;
  }
  * { margin: 0; padding: 0; box-sizing: border-box; }
  html, body { width: 1200px; height: 1000px; overflow: hidden; background: var(--canvas); }
  body { position: relative; font-family: "Montserrat", Arial, sans-serif; }

  .card {
    position: absolute;
    left: 348px;
    width: 503px;
    height: 304px;
    border: 2px solid var(--blue-mid);
    overflow: hidden;
  }
  .card-back { top: 177px; background: var(--white); }
  .card-front { top: 519px; background: var(--blue-mid); border-width: 1px; }

  .band { position: absolute; left: 0; right: 0; height: 26px; display: flex; }
  .band span { flex: 1; }
  .band-top { top: 0; }
  .band-bottom { bottom: 0; }
  .c-light { background: var(--blue-light); }
  .c-dark { background: var(--blue-dark); }
  .c-mid { background: var(--blue-mid); }
  .c-white { background: var(--white); }

  .brand {
    position: absolute;
    left: 0; right: 0; top: 150px;
    text-align: center;
    font-weight: 700;
    font-size: 32px;
    color: var(--blue-dark);
    letter-spacing: 0.5px;
  }
  .brand-mark {
    position: absolute;
    left: 50%; top: 84px;
    width: 52px; height: 52px;
    margin-left: -26px;
    background: var(--blue-dark);
  }
  .tagline {
    position: absolute;
    left: 0; right: 0; top: 224px;
    text-align: center;
    font-weight: 700;
    font-size: 8.5px;
    color: var(--black);
  }

  .details {
    position: absolute;
    left: 39px; top: 72px;
    color: var(--white);
    font-size: 15px;
    line-height: 19px;
  }
  .employee-name { font-weight: 700; font-size: 18.5px; line-height: 24px; }
  .role { margin-bottom: 19px; }
  .details b { font-weight: 700; }
  .address {
    position: absolute;
    left: 0; right: 0; top: 245px;
    text-align: center;
    color: var(--white);
    font-size: 15px;
  }
  .card-front .band-bottom .c-white { border-top: 1px solid var(--blue-mid); }
</style>
</head>
<body>
  <section class="card card-back">
    <div class="band band-top"><span class="c-light"></span><span class="c-dark"></span><span class="c-mid"></span></div>
    <div class="brand-mark"></div>
    <div class="brand">SilverLedgerOak</div>
    <div class="tagline">Helping small to medium business realise their potential</div>
    <div class="band band-bottom"><span class="c-dark"></span><span class="c-light"></span><span class="c-mid"></span></div>
  </section>

  <section class="card card-front">
    <div class="details">
      <div class="employee-name">Employees name</div>
      <div class="role">Role</div>
      <div><b>M</b>: 0000 000 000</div>
      <div><b>P</b>: 1300 847 213</div>
      <div><b>F</b>: 1300 847 286</div>
      <div><b>E</b>: sample@silverledgeroak.com.au</div>
      <div>www.silverledgeroak.com.au</div>
    </div>
    <div class="address">Suite 4 - Level 3/48 Halloran Avenue Parramatta NSW 2150</div>
    <div class="band band-bottom"><span class="c-dark"></span><span class="c-light"></span><span class="c-white"></span></div>
  </section>
</body>
</html>
```